Tolvern Business Cards

Business card design. dont mind if new logo is suggested.
it would be for a security company.
our clients would be bigger security companies around Australia.
have a logo done but can be replaced. see attaached. like the colors.
Need company name, person name, designation, phone and email on front.
At back company logo and name. website saddress and 2 x license numbers
would like to have 2 different background color for both sidde

Industry/Entity Type

Security

Contact Information for Business Card

round corners, front should be light in color. need logo at back with webaddress and 2 x license numners

Font styles to use
Sans Serif

Colors
f37122
faa54b
f8ba93
0255a3
0592cd
85cae6
b3d448
9bcb3c
ffffff

Requirements
Must have
• see description
Nice to have
• see description
Should not have
• should not be difficult to read or hardd to find information on card.. lets say easy on eyes yet catchy

```html
<!DOCTYPE html>
<html lang="en">
<head>
<meta charset="utf-8">
<title>Tolvern Business Cards</title>
<link rel="stylesheet" href="https://fonts.googleapis.com/css2?family=Crimson+Text:wght@600;700&family=Open+Sans:wght@400;600&display=swap">
<style>
  :root {
    --stage: #e7e4df;
    --card-light: #ffffff;
    --card-blue: #0ca4cc;
    --navy: #1b2a5e;
    --teal: #0aa3cb;
    --slate: #6f7d8c;
    --slate-dark: #5f6d7c;
    --white: #ffffff;
  }
  * { box-sizing: border-box; margin: 0; padding: 0; }
  html, body { width: 1200px; height: 1000px; overflow: hidden; }
  body {
    position: relative;
    background: var(--stage);
    font-family: "Open Sans", Arial, sans-serif;
  }
  .card {
    position: absolute;
    left: 266px;
    width: 666px;
    height: 397px;
    border-radius: 24px;
    overflow: hidden;
  }
  .card--front { top: 74px; background: var(--card-light); }
  .card--back { top: 533px; background: var(--card-blue); color: var(--white); text-align: center; }

  .front__decoration {
    position: absolute;
    right: 0; top: 0;
    width: 220px; height: 100%;
    background: radial-gradient(circle at 100% 50%, rgba(10,163,203,0.55) 0%, rgba(10,163,203,0.3) 45%, rgba(27,42,94,0.08) 75%, rgba(255,255,255,0) 100%);
  }
  .person__name {
    position: absolute;
    left: 76px; top: 118px;
    font-family: "Crimson Text", Georgia, serif;
    font-weight: 700;
    font-size: 29px;
    letter-spacing: 0.5px;
    color: var(--navy);
    text-transform: uppercase;
  }
  .person__role {
    position: absolute;
    left: 76px; top: 158px;
    font-size: 16.5px;
    font-weight: 600;
    color: var(--slate-dark);
    text-transform: uppercase;
  }
  .divider {
    position: absolute;
    left: 75px; top: 198px;
    width: 315px; height: 2px;
    background: linear-gradient(90deg, rgba(111,125,140,0.15), rgba(111,125,140,0.7) 40%, rgba(111,125,140,0.15));
  }
  .contact {
    position: absolute;
    left: 74px; top: 220px;
    list-style: none;
    font-size: 17px;
    color: var(--slate);
  }
  .contact li { display: flex; align-items: center; height: 30px; }
  .contact__icon { width: 20px; height: 20px; margin-right: 8px; flex: none; }
  .contact__address { padding-left: 2px; }

  .brand__mark {
    position: absolute;
    left: 293px; top: 116px;
    width: 80px; height: 80px;
    border-radius: 50%;
    background: var(--white);
  }
  .brand__name {
    position: absolute;
    left: 0; right: 0; top: 258px;
    font-family: "Crimson Text", Georgia, serif;
    font-weight: 600;
    font-size: 34px;
    text-transform: uppercase;
    letter-spacing: 0.3px;
  }
  .brand__licences {
    position: absolute;
    left: 0; right: 0; top: 320px;
    font-size: 16px;
  }
  .brand__web {
    position: absolute;
    left: 0; right: 0; top: 347px;
    font-size: 16px;
  }
</style>
</head>
<body>
  <section class="card card--front">
    <div class="front__decoration" role="img" aria-label="Scattered blue dot pattern decoration"></div>
    <h1 class="person__name">Dorin K. Asheby</h1>
    <p class="person__role">Solutions Specialist &amp; Founder</p>
    <div class="divider"></div>
    <ul class="contact">
      <li class="contact__address">14 Calder Lane NSW 2790</li>
      <li>
        <svg class="contact__icon" viewBox="0 0 20 20" aria-hidden="true">
          <circle cx="10" cy="10" r="10" fill="#0aa3cb"/>
          <path d="M5 8.5c0-1.6 2.2-2.6 5-2.6s5 1 5 2.6l-1.6.4-.4-1.4H7l-.4 1.4z M7 9.5h6l1 4H6z" fill="#fff"/>
          <circle cx="10" cy="11.6" r="1.2" fill="#0aa3cb"/>
        </svg>
        0400 123 987
      </li>
      <li>
        <svg class="contact__icon" viewBox="0 0 20 20" aria-hidden="true">
          <circle cx="10" cy="10" r="10" fill="#0aa3cb"/>
          <rect x="5" y="6.5" width="10" height="7" fill="#fff"/>
          <path d="M5 6.5l5 4 5-4" fill="none" stroke="#0aa3cb" stroke-width="1"/>
        </svg>
        dorin@tolvernsecurity.com.au
      </li>
    </ul>
  </section>

  <section class="card card--back">
    <div class="brand__mark"></div>
    <h2 class="brand__name">Tolvern Security Group</h2>
    <p class="brand__licences">000000 | 000000</p>
    <p class="brand__web">www.tolvernsecurity.com.au</p>
  </section>
</body>
</html>
```